Massage-Creme label for a young pharmacy

We are a young pharmacy which is part of a big union. We developed for a customer a very good massage creme with aloe vera, coconut oil, and many more advantages and as well a massage jelly. All we need is a good and affordable label which is beatiful and helps us to promote our product. As we want to develop further products, it would be very cool to have a corporate label for all upcoming products.

Target Market(s)

professional masseurs and physiotherapists

Industry/Entity Type

Health And Wellness

Font styles to use
Sans Serif
Decorative

Colors

Designer to choose colors to be used in the design.

Requirements
Must have
• Professionally looking design (but I'm sure you are doing so... :-)
Nice to have
• Label can have any shape. What you see is just a bad label with corresponding sizes, so you can imagine how it would look like in the final state.
Should not have
• If possible, the label should not be completely black (although it might look cool) as we are printing it on our own Varnick tq318-dm and black is difficult to print (and very costy).

```html
<!DOCTYPE html>
<html lang="de">
<head>
<meta charset="utf-8">
<title>Coconut Aloe Vera – Massage-Crème Label</title>
<link rel="stylesheet" href="https://fonts.googleapis.com/css2?family=Bebas+Neue&family=Roboto:wght@300&family=Sacramento&display=swap">
<style>
  :root {
    --page-bg: #ffffff;
    --label-bg: #e8eae4;
    --ink-dark: #2a2a2a;
    --ink-soft: #6b6d68;
    --aloe-green: #8dbf3c;
    --art-green: #9ccc7a;
    --art-tan: #c9a97a;
  }
  * { margin: 0; padding: 0; box-sizing: border-box; }
  html, body {
    width: 1045px;
    height: 1200px;
    overflow: hidden;
    background: var(--page-bg);
  }
  .label {
    position: absolute;
    left: 262px;
    top: 51px;
    width: 522px;
    height: 1098px;
    background: var(--label-bg);
    overflow: hidden;
  }
  .product-name {
    font-family: "Bebas Neue", "Oswald", "Arial Narrow", sans-serif;
    font-weight: 400;
    text-transform: uppercase;
  }
  .product-name .line {
    position: absolute;
    left: 40px;
    display: block;
    line-height: 1;
    white-space: nowrap;
  }
  .name-coconut { top: 48px;  font-size: 88px;  color: var(--ink-dark); }
  .name-aloe    { top: 116px; font-size: 176px; color: var(--aloe-green); letter-spacing: -4px; }
  .name-vera    { top: 271px; font-size: 121px; color: var(--ink-dark); letter-spacing: -1px; }
  .claims {
    position: absolute;
    left: 42px;
    top: 378px;
    font-family: "Roboto", Arial, sans-serif;
    font-weight: 300;
    font-size: 23px;
    line-height: 24px;
    color: var(--ink-soft);
  }
  .claims p + p { margin-top: 11px; }
  .ingredients-art {
    position: absolute;
    left: 41px;
    top: 505px;
    width: 368px;
    height: 345px;
  }
  .product-type {
    position: absolute;
    left: 58px;
    top: 905px;
    font-family: "Sacramento", cursive;
    font-size: 60px;
    line-height: 1;
    color: var(--ink-dark);
    white-space: nowrap;
  }
</style>
</head>
<body>
  <main class="label">
    <h1 class="product-name">
      <span class="line name-coconut">Coconut</span>
      <span class="line name-aloe">Aloe</span>
      <span class="line name-vera">Vera</span>
    </h1>
    <div class="claims">
      <p>intense<br>moisturizing</p>
      <p>energetisch<br>leitend !</p>
    </div>
    <svg class="ingredients-art" viewBox="0 0 368 345" role="img" aria-label="Photo of sliced aloe vera leaves, a halved coconut and a small bottle of coconut oil">
      <defs>
        <linearGradient id="art-fill" x1="0" y1="0" x2="1" y2="0">
          <stop offset="0" stop-color="var(--art-green)"/>
          <stop offset="0.6" stop-color="#d8d6c6"/>
          <stop offset="1" stop-color="var(--art-tan)"/>
        </linearGradient>
      </defs>
      <rect width="368" height="345" fill="url(#art-fill)" opacity="0.55"/>
    </svg>
    <p class="product-type">Massage-Crème</p>
  </main>
</body>
</html>
```